Business Card & Stationary for Cleaning Company
Business Card, Letterhead, Invoice, Envelope, Fax Cover, Presentation Folder (Letter)
Professional
Brightwave Home Services
Raleigh and Surround Area
Name@brightwavehomeservices.example
www.brightwavehomeservices.example
Please integrate my already-completed company logo (attached) in a clean, modern design for business cards, Fax cover sheet, letterhead, envelopes, Invoice and Presentation Folder (Letter).
Here is my company logo in ai format. Please let me know if there's another format you prefer to work with; I'll try to send that along.
This project is a guaranteed as you can see the link below for the new logo.
http://www.pixelquarry.example/contests/a-logo-for-cleaning-company

```html
<!DOCTYPE html>
<html lang="en">
<head>
<meta charset="utf-8">
<title>Brightwave Home Services – Stationery</title>
<link href="https://fonts.googleapis.com/css2?family=Arimo:wght@400;700&family=Roboto+Condensed:wght@700&display=swap" rel="stylesheet">
<style>
  :root {
    --blue-deep: #0f86c9;
    --blue: #27a6e6;
    --blue-light: #8fd3f5;
    --green: #8cc63f;
    --green-deep: #6aa92a;
    --green-light: #b5dc6a;
    --ink: #4a4a4a;
    --white: #ffffff;
    --paper: #ffffff;
  }
  * { margin: 0; padding: 0; box-sizing: border-box; }
  html, body { width: 1200px; height: 852px; overflow: hidden; background: var(--white); }
  body { position: relative; font-family: "Arimo", Arial, sans-serif; color: var(--ink); }

  .brand { display: flex; align-items: center; gap: 14px; }
  .brand-dot { border-radius: 50%; flex: none; }
  .brand-name { font-family: "Roboto Condensed", "Arial Narrow", sans-serif; font-weight: 700; line-height: 1.05; }

  /* Business card front */
  .card-front {
    position: absolute; left: 5px; top: 5px; width: 571px; height: 206px;
    border-radius: 14px;
    background: radial-gradient(ellipse at 22% 45%, var(--blue-light) 0%, var(--blue) 40%, var(--blue-deep) 100%);
    display: flex; align-items: center; padding-left: 50px;
  }
  .card-front .brand-dot { width: 86px; height: 86px; background: var(--white); opacity: .9; }
  .card-front .brand-name { color: var(--white); font-size: 44px; width: 340px; }

  /* Business card back */
  .card-back {
    position: absolute; left: 5px; top: 240px; width: 571px; height: 216px;
    border-radius: 14px;
    background: linear-gradient(135deg, var(--green-light), var(--green) 55%, var(--green-deep));
    color: var(--white);
  }
  .card-back .details { position: absolute; left: 62px; top: 62px; font-size: 10.5px; line-height: 1.45; text-align: right; width: 210px; }
  .card-back .details .company { font-size: 13px; }
  .card-back .phone { margin-bottom: 10px; }
  .card-back .brand { position: absolute; left: 300px; top: 74px; width: 240px; gap: 10px; }
  .card-back .brand-dot { width: 40px; height: 40px; background: var(--white); }
  .card-back .brand-name { color: var(--white); font-size: 20px; }

  /* Envelope */
  .envelope { position: absolute; left: 5px; top: 470px; width: 571px; height: 375px; }
  .envelope-flap { position: absolute; left: 0; top: 0; }
  .envelope-body {
    position: absolute; left: 0; top: 118px; width: 571px; height: 257px;
    background: var(--paper); border: 2px solid var(--green); border-radius: 0 0 10px 10px; overflow: hidden;
  }
  .recipient { position: absolute; left: 92px; top: 36px; width: 300px; font-size: 11px; color: var(--green-deep); }
  .recipient-line { height: 1px; background: var(--green); margin-left: 24px; margin-top: 20px; }
  .recipient-line:first-of-type { margin-top: -4px; }
  .envelope-band {
    position: absolute; left: 0; bottom: 0; width: 100%; height: 62px;
    background: linear-gradient(90deg, var(--white) 0%, var(--blue-light) 35%, var(--blue) 100%);
  }
  .envelope-band .brand { position: absolute; left: 14px; top: 14px; gap: 8px; }
  .envelope-band .brand-dot { width: 30px; height: 30px; background: var(--blue); }
  .envelope-band .brand-name { color: var(--blue-deep); font-size: 11px; width: 90px; }
  .envelope-band .contact { position: absolute; right: 18px; top: 12px; text-align: right; color: var(--white); font-size: 10px; line-height: 1.4; }

  /* Letterhead */
  .letterhead {
    position: absolute; left: 595px; top: 5px; width: 603px; height: 840px;
    background: var(--paper); border: 2px solid var(--green); border-radius: 4px; overflow: hidden;
  }
  .letterhead .brand { position: absolute; right: 40px; top: 40px; gap: 8px; }
  .letterhead .brand-dot { width: 34px; height: 34px; background: var(--blue); }
  .letterhead .brand-name { color: var(--blue-deep); font-size: 15px; width: 120px; }
  .letterhead-rule { position: absolute; left: 24px; right: 24px; top: 108px; height: 2px; background: var(--green-light); }
  .letterhead-mark {
    position: absolute; left: 230px; top: 560px; width: 270px; height: 190px;
    display: flex; align-items: center; justify-content: center; text-align: center;
  }
  .letterhead-mark .brand-name { color: var(--blue-light); opacity: .45; font-size: 40px; }
  .letterhead-band {
    position: absolute; left: 0; bottom: 40px; width: 100%; height: 62px;
    background: linear-gradient(90deg, var(--white) 0%, var(--blue-light) 40%, var(--blue) 100%);
  }
  .letterhead-band .contact { position: absolute; right: 28px; top: 14px; text-align: right; color: var(--white); font-size: 9.5px; line-height: 1.5; }
</style>
</head>
<body>

  <section class="card-front">
    <div class="brand">
      <span class="brand-dot"></span>
      <span class="brand-name">Brightwave Home Services</span>
    </div>
  </section>

  <section class="card-back">
    <div class="details">
      <div class="company">Brightwave Home Services</div>
      <div class="phone">(919) 555-0142</div>
      <div>2418 Oakmere Drive,</div>
      <div>Suite 210,</div>
      <div>Raleigh NC, 27609</div>
      <div>www.brightwavehomeservices.example</div>
      <div>Name@brightwavehomeservices.example</div>
    </div>
    <div class="brand">
      <span class="brand-dot"></span>
      <span class="brand-name">Brightwave Home Services</span>
    </div>
  </section>

  <section class="envelope">
    <svg class="envelope-flap" width="571" height="124" viewBox="0 0 571 124" aria-hidden="true">
      <defs>
        <linearGradient id="flapGreen" x1="0" y1="0" x2="0" y2="1">
          <stop offset="0" stop-color="#6aa92a"/>
          <stop offset="1" stop-color="#b5dc6a"/>
        </linearGradient>
      </defs>
      <path d="M0 122 C 90 80, 200 20, 270 4 Q 285 0 300 4 C 370 20, 480 80, 571 122 Z" fill="url(#flapGreen)"/>
    </svg>
    <div class="envelope-body">
      <div class="recipient">
        <span>To:</span>
        <div class="recipient-line"></div>
        <div class="recipient-line"></div>
        <div class="recipient-line"></div>
        <div class="recipient-line"></div>
      </div>
      <div class="envelope-band">
        <div class="brand">
          <span class="brand-dot"></span>
          <span class="brand-name">Brightwave Home Services</span>
        </div>
        <div class="contact">
          <div>2418 Oakmere Drive, Suite 210,</div>
          <div>Raleigh NC, 27609</div>
          <div>www.brightwavehomeservices.example &nbsp;|&nbsp; Name@brightwavehomeservices.example</div>
        </div>
      </div>
    </div>
  </section>

  <section class="letterhead">
    <div class="brand">
      <span class="brand-dot"></span>
      <span class="brand-name">Brightwave Home Services</span>
    </div>
    <div class="letterhead-rule"></div>
    <div class="letterhead-mark">
      <span class="brand-name">Brightwave Home Services</span>
    </div>
    <div class="letterhead-band">
      <div class="contact">
        <div>2418 Oakmere Drive, Suite 210,</div>
        <div>Raleigh NC, 27609</div>
        <div>www.brightwavehomeservices.example &nbsp;|&nbsp; Name@brightwavehomeservices.example</div>
      </div>
    </div>
  </section>

</body>
</html>
```